A Gulf Book about Mother - Need Cover Design

An Arabic book tells about the mother, a love letter
Introducing the reader to what the mother is doing for the sake of the family - the tenderness of the baby and a lot of advice to love and respect the mother
The title of the book : السحاب - نغمة ضوء
Meaning in English (clouds - light tune)
The size of the book is small so colors must be bright and expressive
Add to the title of the book
Year - 2018 - 1440
Publishing logo

Target Market(s)
families - student
Requirements
Must have
- Design must be away from any images of people directly
Nice to have
- the book is 150 page that i want The be bright colors give meaning to the message of love from the children to the mother --- for example (hearts - leaves - flowers ... etc)

```html
<!DOCTYPE html>
<html lang="ar" dir="rtl">
<head>
<meta charset="utf-8">
<title>السحاب - نغمة ضوء</title>
<link rel="stylesheet" href="https://fonts.googleapis.com/css2?family=Tajawal:wght@400;500;700&display=swap">
<style>
  :root {
    --title-dark: #3b2a26;
    --title-red: #e0141e;
    --spine-red: #ee0a1d;
    --back-cream: #f8ecd8;
    --body-ink: #3a2e2a;
    --brand-brown: #6b4a1e;
    --white: #ffffff;
  }
  html, body {
    margin: 0;
    padding: 0;
    width: 1200px;
    height: 583px;
    overflow: hidden;
    background: var(--white);
    font-family: "Tajawal", sans-serif;
  }
  .spread {
    position: relative;
    width: 1200px;
    height: 583px;
  }
  .front-cover {
    position: absolute;
    left: 0; top: 0;
    width: 575px; height: 583px;
    overflow: hidden;
  }
  .cover-art {
    position: absolute;
    inset: 0;
    background:
      radial-gradient(ellipse 130px 120px at 172px 300px, #e4202a 0%, #c4141c 65%, rgba(196,20,28,0) 100%),
      radial-gradient(ellipse 420px 300px at 390px 260px, #fbf1e2 0%, rgba(251,241,226,0) 70%),
      linear-gradient(160deg, #e59a3a 0%, #f2c880 35%, #f7e3c6 60%, #eec8ae 100%);
  }
  .cover-title {
    position: absolute;
    left: 104px; top: 62px;
    width: 370px;
    margin: 0;
    font-size: 50px;
    font-weight: 500;
    line-height: 1.2;
    color: var(--title-dark);
    white-space: nowrap;
    direction: rtl;
    text-align: left;
  }
  .cover-title .title-accent { color: var(--title-red); }
  .publisher-mark {
    position: absolute;
    display: flex;
    flex-direction: column;
    align-items: center;
    gap: 5px;
    color: var(--brand-brown);
    font-weight: 700;
    white-space: nowrap;
  }
  .publisher-mark .mark-square {
    width: 42px; height: 42px;
    background: var(--brand-brown);
  }
  .front-publisher { left: 10px; top: 494px; width: 92px; font-size: 11px; }
  .spine {
    position: absolute;
    left: 575px; top: 0;
    width: 49px; height: 583px;
    background: var(--spine-red);
  }
  .spine-title {
    position: absolute;
    left: 50%; top: 294px;
    transform: translate(-50%, -50%) rotate(-90deg);
    color: var(--white);
    font-size: 30px;
    font-weight: 500;
    line-height: 1;
    white-space: nowrap;
    direction: rtl;
  }
  .back-cover {
    position: absolute;
    left: 624px; top: 0;
    width: 576px; height: 583px;
    background: var(--back-cream);
  }
  .back-blurb {
    position: absolute;
    left: 144px; top: 126px;
    width: 300px;
    margin: 0;
    font-size: 13px;
    font-weight: 500;
    line-height: 24.4px;
    color: var(--body-ink);
    text-align: center;
  }
  .back-publisher { left: 250px; top: 478px; width: 92px; font-size: 11px; }
  .isbn-box {
    position: absolute;
    left: 406px; top: 475px;
    width: 130px; height: 79px;
    background: var(--white);
  }
</style>
</head>
<body>
<div class="spread">
  <section class="front-cover">
    <div class="cover-art" role="img" aria-label="صورة يدين تحملان قلبا أحمر ويد طفل تمتد نحوه على خلفية دافئة"></div>
    <h1 class="cover-title"><span class="title-accent">السحاب</span> - نغمة ضوء</h1>
    <div class="publisher-mark front-publisher">
      <span class="mark-square"></span>
      <span>دار النخلة الذهبية</span>
    </div>
  </section>

  <section class="spine">
    <span class="spine-title">السحاب - نغمة ضوء</span>
  </section>

  <section class="back-cover">
    <p class="back-blurb">
      حين تتأمل السحاب تجد فيه نغمة ضوء هادئة<br>
      تشبه دفء البيت حين تعود إليه بعد يوم طويل<br>
      هذا الكتاب رسالة صغيرة من القلب<br>
      إلى كل من يمنح الحب دون انتظار<br>
      صفحات قصيرة تحمل نصائح لطيفة<br>
      عن الاحترام والرحمة والعطاء<br>
      وعن اللحظات التي تبقى في الذاكرة<br>
      كتبت بكلمات بسيطة تناسب الصغار والكبار<br>
      لتقرأها الأسرة معا في المساء<br>
      وتجد فيها ما يجمع القلوب<br>
      ويزرع الأمل في كل بيت<br>
      نغمة ضوء
    </p>
    <div class="publisher-mark back-publisher">
      <span class="mark-square"></span>
      <span>دار النخلة الذهبية</span>
    </div>
    <div class="isbn-box"></div>
  </section>
</div>
</body>
</html>
```